Corporate Business Card Design Project

..Hi designers!
I have established a consultancy within strategic communnications, for which I need a business card design - I've seen some of the things you do in here, and they're great! I'll provide some information in the following:
Name: BriarLedger
Tagline: Guiding Dialogue
Service: Strategic communications consulting (primariy internal communication and optimizing): various organisations - e.g. SMEs, NGOs and NPOs - are offered an analysis of their current efforts and, on the basis of that, management consulting tailored their unique challenges and needs.
It's a sole proprietorship - for now! - but it's my plan to employ 5-20 persons over the years. Therefore the card should NOT symbolize a start-up, but communicate a well-established, serious consultancy. Hence, it should also apply to serious companies and organizations - think Veltra or Hollis Brant Group (both as sender and receiver) ;)
The design should accordingly have a formal, conservative, stylish, corporate, clean look! and ditto colors, eg. black, grey, white etc - corresponding to the logo. The only colour that can appear is the same orange contrast as in my logo (see attachement). Not too bold or dramatic fonds or letters.
I choose the double sided as I think it gives the most professional look: One side with name, titel, phone, e-mail - then a little space - and four additional lines for address.
This composition is if all information should be in the same "column" - feel free to provide suggestions with the address places elsewhere on the one side.
On the other side, I'm only thinkin' something with the logo.
I'd be happy to see different ideas re. the use of the orange contrast, placement of logo, etc.
I do not plan on changing the design of businees cards ever - as I think it is more serious keeping a concept and avoid rebranding - and I'm sure that you can deliver an ever-lasting logo for my company! Thanks :).
Let's play the rest by ear in the correspondance.
Target Market(s)
Executive level: CEOs, HR directors, communication managers/directors, business owners.
Industry/Entity Type
Management Consulting

```html
<!DOCTYPE html>
<html lang="en">
<head>
<meta charset="utf-8">
<title>BriarLedger – Business Card</title>
<link rel="stylesheet" href="https://fonts.googleapis.com/css2?family=Arimo&display=swap">
<style>
  :root {
    --canvas: #e9e7e4;
    --ink: #050505;
    --ink-soft: #1c1c1c;
    --orange: #f28a21;
    --brand-grey: #d4d4d4;
    --tagline-grey: #8a8a8a;
    --white: #ffffff;
  }
  * { box-sizing: border-box; margin: 0; padding: 0; }
  html, body {
    width: 1200px;
    height: 1200px;
    overflow: hidden;
    background: var(--canvas);
  }
  .canvas {
    position: relative;
    width: 1200px;
    height: 1200px;
    font-family: "Arimo", Arial, sans-serif;
  }
  .card {
    position: absolute;
    left: 180px;
    width: 840px;
    height: 480px;
    overflow: hidden;
    box-shadow: 0 10px 30px rgba(0, 0, 0, 0.25);
  }
  .card--front { top: 90px; background: var(--orange); }
  .card--back {
    top: 630px;
    background: radial-gradient(ellipse at 45% 35%, var(--ink-soft) 0%, var(--ink) 70%);
  }

  .front-header {
    position: absolute;
    inset: 0 0 auto 0;
    height: 250px;
    background: linear-gradient(180deg, var(--ink) 0%, var(--ink-soft) 100%);
  }

  /* Brand name placeholder: one font, one weight, one colour */
  .brand {
    position: absolute;
    white-space: nowrap;
  }
  .brand__name {
    display: block;
    font-size: 72px;
    line-height: 1;
    color: var(--brand-grey);
  }
  .brand__tagline {
    display: block;
    font-size: 20px;
    line-height: 1.2;
    color: var(--tagline-grey);
    margin-top: 12px;
  }
  .card--front .brand { left: 70px; top: 80px; }
  .card--back .brand { left: 140px; top: 170px; }
  .card--back .brand__name { font-size: 84px; }
  .card--back .brand__tagline { font-size: 22px; }

  .person {
    position: absolute;
    left: 70px;
    top: 330px;
    color: var(--white);
  }
  .person__name { font-size: 30px; line-height: 1.2; }
  .person__title { font-size: 24px; line-height: 1.2; margin: 8px 0 0 40px; }

  .contact-list {
    position: absolute;
    left: 470px;
    top: 272px;
    list-style: none;
    font-size: 22px;
    color: var(--white);
  }
  .contact-list li {
    display: flex;
    align-items: center;
    gap: 16px;
    height: 46px;
  }
  .contact-list svg { width: 24px; height: 24px; fill: var(--white); flex: none; }
</style>
</head>
<body>
<main class="canvas">

  <section class="card card--front" aria-label="Business card, front">
    <div class="front-header">
      <div class="brand">
        <span class="brand__name">BriarLedger</span>
        <span class="brand__tagline">Guiding Dialogue</span>
      </div>
    </div>

    <ul class="contact-list">
      <li>
        <svg viewBox="0 0 24 24" aria-hidden="true"><path d="M6.6 10.8a15.1 15.1 0 0 0 6.6 6.6l2.2-2.2a1 1 0 0 1 1-.25 11.4 11.4 0 0 0 3.6.57 1 1 0 0 1 1 1V20a1 1 0 0 1-1 1A17 17 0 0 1 3 4a1 1 0 0 1 1-1h3.5a1 1 0 0 1 1 1c0 1.25.2 2.45.57 3.57a1 1 0 0 1-.25 1z"/></svg>
        <span>phone</span>
      </li>
      <li>
        <svg viewBox="0 0 24 24" aria-hidden="true"><path d="M2 5h20v2l-10 6L2 7z"/><path d="M2 9l10 6 10-6v10H2z"/></svg>
        <span>e-mail</span>
      </li>
      <li>
        <svg viewBox="0 0 24 24" aria-hidden="true"><path d="M12 2a7 7 0 0 0-7 7c0 5.2 7 13 7 13s7-7.8 7-13a7 7 0 0 0-7-7zm0 9.5A2.5 2.5 0 1 1 12 6.5a2.5 2.5 0 0 1 0 5z"/></svg>
        <span>address</span>
      </li>
    </ul>

    <div class="person">
      <p class="person__name">Name</p>
      <p class="person__title">Title</p>
    </div>
  </section>

  <section class="card card--back" aria-label="Business card, back">
    <div class="brand">
      <span class="brand__name">BriarLedger</span>
      <span class="brand__tagline">Guiding Dialogue</span>
    </div>
  </section>

</main>
</body>
</html>
```